Bramwell Exteriors Needs a New Website!

We are an exteriors company specializing in vinyl siding, Peter Aldous siding, aluminum soffit/fascia, trough. We do new construction work as well as renovations. We also build detached garages.
You can view our current website at www.bramwellbuilders.ca
I want to completely overhaul the website.
Our services are different now as we no longer do new home construction as well as we do not do the snow clearing.
I want to focus on 2 things in particular on the website:

1/ Exterior renovations

2/ Detached Garage construction.

I have included our logo in the attached files to use as well.

Some features we would like:

1/ Be able to easily attach a video from Youtube/Vimeo to highlight a product or service
2/ Quick chat or contact button that we can talk to a potential client quickly
3/ Meet the Team page that is interesting and fresh
4/ Place for us to put in helpful exterior tips/suggestions for homeowners.

Content is not important, but looking for the best design that will attract people once they click on our page and want to renovate with us.

Target Market(s)

People looking for renovations on their home, people looking to build a detached garage.

Industry/Entity Type

Residential Construction

Coding

Coded - Design and coding required

Number of Pages Required

5+ page

Font styles to use
Sans Serif

Requirements
Must have
• Fresh and exciting home page.

Simple design. Don't want it over complicated or too much information to confuse the potential client.

Easy way to contact us.

Meet the team page that instills confidence
Nice to have
• Colour of website to go off our logo. Doesn't need to be an exact match, but something that goes well with our blue and grey.

```html
<!DOCTYPE html>
<html lang="en">
<head>
<meta charset="utf-8">
<title>Bramwell Exteriors</title>
<link rel="stylesheet" href="https://fonts.googleapis.com/css2?family=Montserrat:wght@400;500;600;700;800&family=Roboto:wght@400;500;700&family=Roboto+Condensed:wght@700&display=swap">
<style>
:root{
  --blue:#1a5fb4;
  --blue-dark:#124e9c;
  --blue-soft:#e6eef8;
  --ink:#1d1d1f;
  --grey:#55565c;
  --mist:#f3f0ef;
  --line:#d9d9de;
  --white:#ffffff;
}
*{box-sizing:border-box;margin:0;padding:0}
html,body{width:1200px;height:4132px;overflow:hidden}
body{position:relative;font-family:"Roboto",Arial,sans-serif;color:var(--ink);background:var(--white)}
.abs{position:absolute}
.heading{font-family:"Montserrat",Arial,sans-serif;font-weight:700;text-transform:uppercase}
.section-title{position:absolute;left:0;width:1200px;text-align:center;font-family:"Montserrat",Arial,sans-serif;font-weight:700;font-size:29px;color:var(--ink)}
.title-rule{position:absolute;left:579px;width:42px;height:8px;border-top:3px solid var(--blue);border-bottom:2px solid var(--grey)}
.btn{position:absolute;display:flex;align-items:center;justify-content:center;background:var(--blue);color:var(--white);font-family:"Montserrat",Arial,sans-serif;font-weight:700;font-size:12px;text-transform:uppercase;border-radius:3px}

/* header */
.brand{display:flex;align-items:center;gap:12px}
.brand-dot{width:56px;height:56px;border-radius:50%;background:var(--blue)}
.brand-name{font-family:"Montserrat",Arial,sans-serif;font-weight:800;font-size:26px;line-height:1.05;color:var(--blue);text-transform:uppercase}
.follow{left:711px;top:33px;font-family:"Montserrat",Arial,sans-serif;font-size:11px;font-weight:600}
.social-dot{position:absolute;top:29px;width:26px;height:26px;border-radius:50%;background:var(--blue)}
.call-label{left:935px;top:20px;font-family:"Montserrat",Arial,sans-serif;font-size:11px;font-weight:600}
.call-number{left:935px;top:33px;font-family:"Roboto Condensed",Arial,sans-serif;font-weight:700;font-size:28px;color:var(--blue)}
.nav{position:absolute;top:76px;left:560px;display:flex;font-family:"Montserrat",Arial,sans-serif;font-size:13.5px;font-weight:500;text-transform:uppercase}
.nav a{color:var(--ink);text-decoration:none;padding:3px 7px;margin-right:7px}
.nav a.active{background:var(--blue);color:var(--white)}

/* hero */
.hero{left:0;top:0;width:1200px;height:622px;background:linear-gradient(180deg,#8fb8e4 0%,#c4d9ee 30%,#7b6a5c 55%,#5d4a3c 72%,#4f8a38 85%,#3f7a2c 100%);z-index:-1}
.hero-panel{left:133px;top:212px;width:322px;height:242px;background:rgba(255,255,255,.85)}
.hero-title{left:162px;top:242px;width:280px;font-size:32px;line-height:37px;color:var(--blue);font-weight:800;white-space:nowrap}
.hero-btn{left:162px;top:377px;width:218px;height:42px;font-size:16px}
.dot{position:absolute;top:583px;width:9px;height:9px;border-radius:50%;background:rgba(255,255,255,.8)}
.dot.on{background:var(--blue);box-shadow:0 0 0 2px #fff}

/* services */
.services{left:0;top:622px;width:1200px;height:639px;background:var(--mist)}
.card{position:absolute;width:454px;height:205px;background:var(--white);overflow:hidden;box-shadow:0 2px 8px rgba(0,0,0,.05)}
.card-badge{position:absolute;left:-5px;top:-5px;width:106px;height:106px;border-radius:50%;background:var(--blue-soft);display:flex;align-items:center;justify-content:center}
.card-rule{position:absolute;left:138px;top:32px;width:1px;height:136px;background:var(--line)}
.card-title{position:absolute;left:176px;top:30px;font-size:15px;line-height:20px;font-weight:700}
.card-text{position:absolute;left:176px;top:82px;width:230px;font-size:13px;line-height:17px;color:#333}
.card-link{position:absolute;left:178px;top:154px;font-family:"Montserrat",Arial,sans-serif;font-size:11px;font-weight:700;color:var(--blue);text-decoration:underline}

/* feature banners */
.feature{position:absolute;top:1261px;width:600px;height:374px;text-align:center}
.feature-renos{left:0;background:linear-gradient(180deg,#2f73c9 0%,#6ea2de 45%,#3e4a44 70%,#2d3530 100%)}
.feature-garage{left:600px;background:linear-gradient(180deg,#8fb4e6 0%,#c5d9f3 45%,#3b3a3a 65%,#b8b9b4 85%,#7a5b3e 100%)}
.feature h3{position:absolute;left:0;right:0;top:40px;font-size:21px}
.feature p{position:absolute;left:0;right:0;top:74px;font-size:13.5px;line-height:18px}
.feature .btn{top:128px;left:270px;width:95px;height:26px;font-size:11px}

/* why us */
.why-item{position:absolute;width:250px}
.why-item h4{font-family:"Montserrat",Arial,sans-serif;font-weight:700;font-size:13px;margin-bottom:6px}
.why-item p{font-size:12.5px;line-height:17px;color:#444}
.why-icon{position:absolute;width:58px;height:58px;border-radius:50%;background:var(--blue);display:flex;align-items:center;justify-content:center}
.why-mark{left:483px;top:1833px;width:234px;height:234px;border-radius:50%;border:14px solid var(--grey);display:flex;align-items:center;justify-content:center}
.why-mark span{font-family:"Montserrat",Arial,sans-serif;font-weight:800;font-size:28px;color:var(--blue)}

/* work */
.work{left:0;top:2153px;width:1200px;height:534px;background:linear-gradient(180deg,#e9e9ec 0%,#dfe0e3 100%)}
.work-tile{position:absolute;top:2326px;width:222px;height:231px}
.arrow{position:absolute;font-family:"Montserrat",Arial,sans-serif;font-size:34px;color:var(--grey)}

/* team */
.member{position:absolute;top:2866px;width:200px;text-align:center}
.portrait{margin:0 auto;width:186px;height:186px;border-radius:50%;border:4px solid #fff;box-shadow:0 0 0 1px #d5d5d9;background:linear-gradient(180deg,#9aa36c 0%,#7d8a53 55%,#5e6b82 100%)}
.member h5{margin-top:22px;font-size:14px;font-weight:700}
.member .role{font-size:13.5px;color:#444;margin-top:3px}
.member .bio{display:inline-block;margin-top:14px;width:77px;height:25px;line-height:21px;border:2px solid var(--blue);border-radius:3px;font-family:"Montserrat",Arial,sans-serif;font-size:10px;font-weight:700;color:var(--blue)}
.team-arrow{position:absolute;top:2945px;width:26px;height:26px;border-radius:50%;background:#c9c9cd}

/* video */
.video{left:0;top:3296px;width:1200px;height:441px;background:linear-gradient(180deg,#6f7fa3 0%,#b6a9a7 35%,#c49f7e 55%,#3a3a2c 75%,#1f2a1c 100%)}
.video h2{position:absolute;left:0;right:0;top:40px;text-align:center;color:#fff;font-family:"Montserrat",Arial,sans-serif;font-weight:600;font-size:27px}
.video p{position:absolute;left:0;right:0;top:86px;text-align:center;color:#fff;font-size:19px}
.play{position:absolute;left:565px;top:240px;width:70px;height:70px;border-radius:50%;background:#fff;display:flex;align-items:center;justify-content:center}

/* footer */
.footer{left:0;top:3737px;width:1200px;height:395px;background:var(--blue);color:#fff}
.footer .brand-dot{background:#fff}
.footer .brand-name{color:#fff;font-size:30px}
.foot-head{position:absolute;top:62px;font-family:"Montserrat",Arial,sans-serif;font-weight:700;font-size:15px}
.foot-menu{position:absolute;left:494px;top:100px;list-style:none;font-size:13.5px;line-height:24px;text-transform:uppercase}
.foot-row{position:absolute;display:flex;gap:12px;font-size:13px;line-height:18px}
.foot-icon{flex:none;width:26px;height:26px;border-radius:50%;background:#fff;display:flex;align-items:center;justify-content:center}
.copyright{position:absolute;left:0;right:0;top:352px;text-align:center;font-size:11.5px}
</style>
</head>
<body>

<!-- header & hero -->
<div class="abs hero" role="img" aria-label="Photo of a large two-storey house with brown siding, white trim and green lawn under a blue sky"></div>
<div class="abs brand" style="left:133px;top:22px">
  <div class="brand-dot"></div>
  <div class="brand-name">Bramwell<br>Exteriors</div>
</div>
<div class="abs follow">FOLLOW</div>
<div class="social-dot" style="left:771px" aria-label="Friendpage"></div>
<div class="social-dot" style="left:805px" aria-label="Chirper"></div>
<div class="social-dot" style="left:839px" aria-label="ProLink"></div>
<svg class="abs" style="left:890px;top:26px" width="34" height="34" viewBox="0 0 24 24" fill="none" stroke="#55565c" stroke-width="1.6"><path d="M5 3h4l2 5-3 2a11 11 0 0 0 6 6l2-3 5 2v4a2 2 0 0 1-2 2A17 17 0 0 1 3 5a2 2 0 0 1 2-2z"/></svg>
<div class="abs call-label">CALL US NOW</div>
<div class="abs call-number">780-555-0142</div>
<nav class="nav">
  <a class="active">Home</a><a>About Us</a><a>Services</a><a>Meet The Team</a><a>Request A Quote</a>
</nav>

<div class="abs hero-panel"></div>
<h1 class="abs heading hero-title">Experience<br>The Bramwell<br>Difference</h1>
<div class="btn hero-btn">Contact Us</div>
<div class="dot" style="left:557px"></div>
<div class="dot" style="left:577px"></div>
<div class="dot on" style="left:598px"></div>
<div class="dot" style="left:618px"></div>
<div class="dot" style="left:638px"></div>

<!-- services -->
<div class="abs services"></div>
<h2 class="section-title" style="top:664px">OUR SERVICES</h2>
<div class="title-rule" style="top:716px"></div>

<div class="card" style="left:133px;top:778px">
  <div class="card-badge"><svg width="56" height="56" viewBox="0 0 24 24" fill="#1a5fb4"><path d="M12 2 1 10h3v11h16V10h3z"/><rect x="7" y="12" width="10" height="9" fill="#fff"/><path d="M7 14.5h10M7 17h10M7 19.5h10" stroke="#1a5fb4" stroke-width="1"/></svg></div>
  <div class="card-rule"></div>
  <div class="card-title">DETACHED<br>GARAGES</div>
  <div class="card-text">Bramwell Builders designs and builds sturdy detached garages that suit your home.</div>
  <div class="card-link">READ MORE</div>
</div>
<div class="card" style="left:605px;top:778px">
  <div class="card-badge"><svg width="60" height="56" viewBox="0 0 26 24" fill="#1a5fb4"><path d="M13 2 1 11h3v11h18V11h3z"/><rect x="7" y="13" width="4" height="4" fill="#fff"/><rect x="15" y="13" width="4" height="4" fill="#fff"/></svg></div>
  <div class="card-rule"></div>
  <div class="card-title">NEW HOME<br>EXTERIORS</div>
  <div class="card-text">Bramwell's exterior division is Edmonton's exterior finishing experts.</div>
  <div class="card-link">READ MORE</div>
</div>
<div class="card" style="left:133px;top:999px">
  <div class="card-badge"><svg width="56" height="56" viewBox="0 0 24 24" fill="none" stroke="#1a5fb4" stroke-width="2.4" stroke-linecap="round"><path d="M4 4l7 7M14 13l6 6"/><path d="M17 3l-9 9 3 3 9-9z" fill="#1a5fb4"/></svg></div>
  <div class="card-rule"></div>
  <div class="card-title">EXTERIOR<br>RENOVATIONS</div>
  <div class="card-text">Looking for a reputable company to replace that aging siding?</div>
  <div class="card-link">READ MORE</div>
</div>
<div class="card" style="left:605px;top:999px">
  <div class="card-badge"><svg width="56" height="56" viewBox="0 0 24 24" fill="none" stroke="#1a5fb4" stroke-width="2" stroke-linecap="round"><path d="M3 6h18M3 10h18M3 14h18M3 18h18"/><path d="M19 6v14" stroke-width="2.6"/></svg></div>
  <div class="card-rule"></div>
  <div class="card-title">SIDING &amp;<br>SOFFIT</div>
  <div class="card-text">Vinyl and fibre cement siding, aluminum soffit, fascia and eavestrough done right.</div>
  <div class="card-link">READ MORE</div>
</div>

<!-- feature banners -->
<div class="feature feature-renos" role="img" aria-label="Photo of a renovated craftsman-style house with grey siding under a blue sky">
  <h3 class="heading" style="color:#fff">Exterior Renovations</h3>
  <p style="color:#fff">Lorem Ipsum is simply dummy text of the<br>printing and typesetting industry</p>
  <div class="btn" style="background:#fff;color:var(--blue)">Read More</div>
</div>
<div class="feature feature-garage" role="img" aria-label="Photo of a detached garage with a wide grey door and lit windows">
  <h3 class="heading" style="color:#2a2a2a">Detached Garage Construction</h3>
  <p style="color:#2a2a2a">Lorem Ipsum is simply dummy text of the<br>printing and typesetting industry</p>
  <div class="btn">Read More</div>
</div>

<!-- why us -->
<h2 class="section-title" style="top:1706px">WHY US</h2>
<div class="title-rule" style="top:1760px"></div>
<div class="abs why-mark"><span>BRAMWELL</span></div>

<div class="why-icon" style="left:131px;top:1716px"><svg width="30" height="30" viewBox="0 0 24 24" fill="#fff"><path d="M12 2 4 5v6c0 5 3.5 9 8 11 4.5-2 8-6 8-11V5z"/></svg></div>
<div class="why-item" style="left:210px;top:1714px"><h4>CERTIFIED EXPERIENCE</h4><p>Having professionals do the job gives you the confidence that the job will be done right, on budget, and on time.</p></div>
<div class="why-icon" style="left:131px;top:1851px"><svg width="30" height="30" viewBox="0 0 24 24" fill="#fff"><path d="M3 5h18v11H9l-5 4v-4H3z"/><circle cx="8" cy="10.5" r="1.3" fill="#1a5fb4"/><circle cx="12" cy="10.5" r="1.3" fill="#1a5fb4"/><circle cx="16" cy="10.5" r="1.3" fill="#1a5fb4"/></svg></div>
<div class="why-item" style="left:210px;top:1850px"><h4>SUPERIOR COMMUNICATION</h4><p>Taking the time to explain the construction process and promptly answering the phone or email is what sets us apart from others.</p></div>
<div class="why-icon" style="left:131px;top:1987px"><svg width="30" height="30" viewBox="0 0 24 24" fill="none" stroke="#fff" stroke-width="2"><circle cx="12" cy="9" r="6"/><path d="M3 19c3 0 5 2 9 2s6-2 9-4" stroke-linecap="round"/></svg></div>
<div class="why-item" style="left:210px;top:1986px"><h4>COMPETITIVE PRICING</h4><p>Although we offer the best in services, we won't blow your budget on the job. We also take credit cards in our renovations division.</p></div>

<div class="why-icon" style="left:1030px;top:1716px"><svg width="28" height="28" viewBox="0 0 24 24" fill="#fff"><path d="M2 10h4v11H2zM8 10l4-8c2 0 3 1 2.5 3L14 9h6a2 2 0 0 1 2 2.4l-1.6 7.6A2 2 0 0 1 18.4 21H8z"/></svg></div>
<div class="why-item" style="left:768px;top:1714px"><h4>GUARANTEED SATISFACTION</h4><p>We aren't happy unless you are. Along with a robust limited lifetime warranty on our work, we ensure you are satisfied even years after completion.</p></div>
<div class="why-icon" style="left:1030px;top:1851px"><svg width="28" height="28" viewBox="0 0 24 24" fill="#fff"><rect x="4" y="10" width="16" height="12" rx="2"/><path d="M8 10V7a4 4 0 0 1 8 0v3" fill="none" stroke="#fff" stroke-width="2.4"/></svg></div>
<div class="why-item" style="left:768px;top:1850px"><h4>SAFETY CONSCIENCE</h4><p>COR certification, liability insurance, and WCB coverage on all workers gives you peace of mind that the job will be done safely.</p></div>
<div class="why-icon" style="left:1030px;top:1987px"><svg width="30" height="30" viewBox="0 0 24 24" fill="none" stroke="#fff" stroke-width="2.6"><circle cx="13" cy="10" r="4"/><path d="M13 2v3M13 15v3M5 10h3M18 10h3M7.5 4.5l2 2M16.5 13.5l2 2M7.5 15.5l2-2M16.5 6.5l2-2"/><circle cx="6" cy="19" r="2"/></svg></div>
<div class="why-item" style="left:768px;top:1986px"><h4>UNRIVALLED QUALITY</h4><p>Our greatest asset is our unrivalled pursuit of a "top of the line" job each and every time.</p></div>

<!-- our work -->
<div class="abs work"></div>
<h2 class="section-title" style="top:2207px">OUR WORK</h2>
<div class="title-rule" style="top:2260px"></div>
<div class="arrow" style="left:72px;top:2420px">&#8249;</div>
<div class="arrow" style="left:1098px;top:2420px">&#8250;</div>
<div class="work-tile" style="left:131px;background:linear-gradient(180deg,#b9c3cf 0%,#6e5a48 60%,#3d3228 100%)" role="img" aria-label="Photo of a house front with stone columns and a gabled porch"></div>
<div class="work-tile" style="left:370px;background:linear-gradient(135deg,#7d4a3a 0%,#a86a55 45%,#3d4a66 100%)" role="img" aria-label="Photo of a timber staircase under construction"></div>
<div class="work-tile" style="left:606px;background:linear-gradient(180deg,#8799b4 0%,#b48a5e 55%,#3c3126 100%)" role="img" aria-label="Photo of a modern wooden home lit at dusk"></div>
<div class="work-tile" style="left:845px;background:linear-gradient(160deg,#6b5a4f 0%,#3e4452 50%,#d9dde4 100%)" role="img" aria-label="Photo of a dark shingle-sided house roofline in snow"></div>
<div class="btn" style="left:531px;top:2600px;width:145px;height:31px">View All Works</div>

<!-- team -->
<h2 class="section-title" style="top:2743px">TEAM</h2>
<div class="title-rule" style="top:2796px"></div>
<div class="team-arrow" style="left:46px"></div>
<div class="team-arrow" style="left:1119px"></div>
<div class="member" style="left:96px"><div class="portrait" role="img" aria-label="Portrait of Colin Ashby outdoors"></div><h5>Colin Ashby</h5><div class="role">General Manager</div><div class="bio">VIEW BIO</div></div>
<div class="member" style="left:295px"><div class="portrait" role="img" aria-label="Portrait of Owen Pritchard outdoors"></div><h5>Owen Pritchard</h5><div class="role">Operations Manager</div><div class="bio">VIEW BIO</div></div>
<div class="member" style="left:500px"><div class="portrait" role="img" aria-label="Portrait of Tobias Vermeer outdoors"></div><h5>Tobias Vermeer</h5><div class="role">Field Service Manager</div><div class="bio">VIEW BIO</div></div>
<div class="member" style="left:699px"><div class="portrait" role="img" aria-label="Portrait of Silas Hartley outdoors"></div><h5>Silas Hartley</h5><div class="role">Site Supervisor</div><div class="bio">VIEW BIO</div></div>
<div class="member" style="left:898px"><div class="portrait" role="img" aria-label="Portrait of Gideon Hartley outdoors"></div><h5>Gideon Hartley</h5><div class="role">Renovations Manager</div><div class="bio">VIEW BIO</div></div>
<div class="btn" style="left:541px;top:3205px;width:127px;height:29px">View All Team</div>

<!-- video -->
<div class="abs video" role="img" aria-label="Video still of a modern timber house glowing at sunset">
  <h2>OUR VIDEO</h2>
  <p>Lorem Ipsum is simply dummy text of the printing</p>
  <div class="play"><svg width="40" height="40" viewBox="0 0 24 24"><circle cx="12" cy="12" r="11" fill="none" stroke="#1a5fb4" stroke-width="2"/><path d="M9 7l8 5-8 5z" fill="#1a5fb4"/></svg></div>
</div>

<!-- footer -->
<footer class="abs footer">
  <div class="abs brand" style="left:133px;top:104px">
    <div class="brand-dot"></div>
    <div class="brand-name">Bramwell<br>Exteriors</div>
  </div>
  <div class="foot-head" style="left:494px">MENU</div>
  <ul class="foot-menu"><li>Home</li><li>About Us</li><li>Services</li><li>Meet The Team</li><li>Request A Quote</li></ul>

  <div class="foot-head" style="left:687px">CONTACT US</div>
  <div class="foot-row" style="left:685px;top:104px"><div class="foot-icon"><svg width="14" height="14" viewBox="0 0 24 24" fill="#1a5fb4"><path d="M12 2a7 7 0 0 0-7 7c0 5 7 13 7 13s7-8 7-13a7 7 0 0 0-7-7zm0 10a3 3 0 1 1 0-6 3 3 0 0 1 0 6z"/></svg></div><div>2150 Alder Street<br>Riverton, CA 90412</div></div>
  <div class="foot-row" style="left:685px;top:166px"><div class="foot-icon"><svg width="14" height="14" viewBox="0 0 24 24" fill="#1a5fb4"><path d="M5 3h4l2 5-3 2a11 11 0 0 0 6 6l2-3 5 2v4a2 2 0 0 1-2 2A17 17 0 0 1 3 5a2 2 0 0 1 2-2z"/></svg></div><div>Call Us<br>780-555-0142</div></div>
  <div class="foot-row" style="left:685px;top:227px"><div class="foot-icon"><svg width="14" height="14" viewBox="0 0 24 24" fill="#1a5fb4"><path d="M2 5h20v14H2z"/><path d="M2 5l10 8 10-8" fill="none" stroke="#fff" stroke-width="2"/></svg></div><div>E mail Us<br>info@bramwellbuilders.ca</div></div>

  <div class="foot-head" style="left:946px">FOLLOW US</div>
  <div class="foot-row" style="left:946px;top:104px"><div class="foot-icon"></div><div>Like us on<br>FRIENDPAGE</div></div>
  <div class="foot-row" style="left:946px;top:166px"><div class="foot-icon"></div><div>Follow us on<br>CHIRPER</div></div>
  <div class="foot-row" style="left:946px;top:227px"><div class="foot-icon"></div><div>Follow us on<br>PROLINK</div></div>

  <div class="copyright">Copyright © 2020 All Rights Reserved</div>
</footer>

</body>
</html>
```